New career and executive coaching business needs a business card design including logo

Company name: 'Harbourline Career Partners.' The aim of my coaching engagements is to help people improve their communication in the workplace and achieve their career goals. The process involves working with individuals to help them uncover their strengths and talents, then leverage those to improve their working lives. The Tellwood Inventory is the starting point to the process. I am after an exciting and interesting business card design (including logo)which is professional yet will still get people's attention.

Industry/Entity Type

Business

Contact Information for Business Card

Name: Gavin Holloway
Position: Owner
Address: 58 Pellimore Cres, Wardell Vic 3197
Phone: 0481937145
Website: harbourlinecareer.com.au
Email: gavin@hcp.com.au

Colors
33a6d7
00a990
0355a3
3176b5

Requirements
Must have
• logo

```html
<!DOCTYPE html>
<html lang="en">
<head>
<meta charset="utf-8">
<title>Harbourline Career Partners – Business Card</title>
<link rel="stylesheet" href="https://fonts.googleapis.com/css2?family=Roboto+Condensed:wght@400;700&family=Questrial&family=Cabin:wght@700&display=swap">
<style>
  :root {
    --bg: #d2d2d2;
    --paper: #f0f0f0;
    --brand-blue: #0a6ca3;
    --ink: #3a3a3a;
    --band-grey: #a9a9aa;
    --on-blue: #f4f6f8;
  }
  * { margin: 0; padding: 0; box-sizing: border-box; }
  html, body { width: 1200px; height: 754px; overflow: hidden; }
  body { background: var(--bg); position: relative; font-family: "Questrial", sans-serif; }

  .card {
    position: absolute;
    top: 242px;
    width: 459px;
    height: 255px;
    overflow: hidden;
  }
  .card--front { left: 120px; background: var(--paper); }
  .card--back { left: 624px; background: var(--brand-blue); }

  .holder { position: absolute; left: 30px; top: 54px; }
  .holder__name {
    font-family: "Cabin", sans-serif;
    font-weight: 700;
    font-size: 14px;
    color: var(--brand-blue);
    letter-spacing: 0.1px;
    text-transform: uppercase;
  }
  .holder__role { font-size: 12px; color: var(--ink); margin-top: 1px; }

  .wordmark {
    position: absolute;
    display: flex;
    align-items: center;
    gap: 9px;
    font-family: "Roboto Condensed", sans-serif;
    font-weight: 400;
  }
  .wordmark__dot { border-radius: 50%; flex: none; }
  .wordmark__text { line-height: 1; }
  .wordmark__line1 { display: block; text-transform: uppercase; }
  .wordmark__line2 { display: block; margin-top: 3px; }

  .card--front .wordmark { right: 26px; top: 48px; color: var(--brand-blue); }
  .card--front .wordmark__dot { width: 18px; height: 18px; background: var(--brand-blue); }
  .card--front .wordmark__line1 { font-size: 27px; }
  .card--front .wordmark__line2 { font-size: 15px; }

  .card--back .wordmark { left: 50%; top: 106px; transform: translateX(-50%); color: var(--on-blue); }
  .card--back .wordmark__dot { width: 22px; height: 22px; background: var(--on-blue); }
  .card--back .wordmark__line1 { font-size: 32px; }
  .card--back .wordmark__line2 { font-size: 17px; }

  .contacts { position: absolute; left: 30px; top: 179px; list-style: none; }
  .contacts li {
    display: flex; align-items: center; gap: 6px;
    font-size: 11.5px; color: var(--ink); height: 14.5px;
  }
  .contacts svg { width: 11px; height: 11px; flex: none; }

  .address {
    position: absolute; right: 25px; top: 194px;
    font-size: 11.5px; color: var(--ink); text-align: right; line-height: 14.5px;
    font-style: normal;
  }
  .edge-band { position: absolute; left: 0; bottom: 0; width: 459px; height: 12px; }
</style>
</head>
<body>
  <section class="card card--front">
    <div class="holder">
      <div class="holder__name">Gavin Holloway</div>
      <div class="holder__role">Owner</div>
    </div>

    <div class="wordmark">
      <span class="wordmark__dot"></span>
      <span class="wordmark__text">
        <span class="wordmark__line1">Harbourline</span>
        <span class="wordmark__line2">Career Partners</span>
      </span>
    </div>

    <ul class="contacts">
      <li>
        <svg viewBox="0 0 11 11"><rect width="11" height="11" rx="2" fill="#0a6ca3"/><path d="M3.3 2.2l1.3 1.7-.7.8c.4 1 1.1 1.7 2 2.1l.8-.7 1.7 1.3-.6 1.2C5.4 8.4 2.7 5.7 2.1 2.8z" fill="#fff"/></svg>
        <span>0481937145</span>
      </li>
      <li>
        <svg viewBox="0 0 11 11"><rect width="11" height="11" rx="2" fill="#0a6ca3"/><rect x="2" y="3" width="7" height="5" fill="none" stroke="#fff" stroke-width="0.9"/><path d="M2 3l3.5 2.8L9 3" fill="none" stroke="#fff" stroke-width="0.9"/></svg>
        <span>gavin@hcp.com.au</span>
      </li>
      <li>
        <svg viewBox="0 0 11 11"><rect width="11" height="11" rx="2" fill="#0a6ca3"/><circle cx="5.5" cy="5.5" r="3.3" fill="none" stroke="#fff" stroke-width="0.8"/><ellipse cx="5.5" cy="5.5" rx="1.4" ry="3.3" fill="none" stroke="#fff" stroke-width="0.8"/><path d="M2.2 5.5h6.6" stroke="#fff" stroke-width="0.8"/></svg>
        <span>www.harbourlinecareer.com.au</span>
      </li>
    </ul>

    <address class="address">58 Pellimore Cres<br>Wardell Vic 3197</address>

    <svg class="edge-band" viewBox="0 0 459 12" preserveAspectRatio="none">
      <polygon points="0,3 209,3 200,12 0,12" fill="var(--band-grey)"/>
      <polygon points="216,0 459,0 459,12 204,12" fill="var(--brand-blue)"/>
    </svg>
  </section>

  <section class="card card--back">
    <div class="wordmark">
      <span class="wordmark__dot"></span>
      <span class="wordmark__text">
        <span class="wordmark__line1">Harbourline</span>
        <span class="wordmark__line2">Career Partners</span>
      </span>
    </div>
  </section>
</body>
</html>
```